New design for www.tolvadera.com

New Web design for www.tolvadera.com.

We strongly encourage to see the actual design, and make proposal, as we find the best proyect we can increase the budget if necessary.
Wordpress, Joomla... not a problem

Best regards

Benedict
Updates

More time, for better proyect choice

Enfermo

Enfermo

Enfermo

Target Market(s)

Industria alimentaria, Zelkor clients, government organization

Industry/Entity Type

Food blog

Coding

Coded - Design and coding required

Number of Pages Required

5+ page

Font styles to use
Sans Serif

Requirements
Must have
• Fanpage and Instagram link
ChatLine API to direct message
Great design (we process cereal as amaranth and quinoa)
Nice to have
• See the actual section in the original webpage.

```html
<!DOCTYPE html>
<html lang="en">
<head>
<meta charset="utf-8">
<title>Tolvadera — Quality Low Prices</title>
<link rel="stylesheet" href="https://fonts.googleapis.com/css2?family=Lato:wght@400;700&family=Poppins:wght@600;700&family=Kaushan+Script&display=swap">
<style>
:root{
  --ink:#1b0a08;
  --red:#f42222;
  --red-deep:#e01b1b;
  --gold:#f3b41b;
  --gold-soft:#f7c33a;
  --cream:#fdf3df;
  --white:#ffffff;
  --panel:#1c1c1c;
  --text:#222222;
}
*{box-sizing:border-box;margin:0;padding:0}
html,body{width:1200px;height:3683px;overflow:hidden}
body{position:relative;background:var(--cream);font-family:"Lato",sans-serif;color:var(--text)}
.abs{position:absolute}
.waves{position:absolute;left:0;top:0;width:1200px;height:3683px}
.btn{position:absolute;display:flex;align-items:center;justify-content:center;background:var(--red);color:var(--white);border-radius:20px;font-family:"Poppins",sans-serif;font-weight:600;font-size:13px}
.heading{font-family:"Poppins",sans-serif;font-weight:700;color:var(--red);font-size:34px;letter-spacing:.5px}

/* nav */
.topbar{left:0;top:0;width:1200px;height:94px;background:var(--ink)}
.brand{left:157px;top:28px;display:flex;align-items:center;gap:10px;color:var(--red);font-family:"Lato",sans-serif;font-weight:700;font-size:22px}
.brand-dot{width:26px;height:26px;border-radius:50%;background:var(--gold)}
.menu{left:345px;top:32px;display:flex;gap:37px;color:#fff;font-size:17px}
.lang{left:1001px;top:34px;color:#fff;font-size:14px;display:flex;gap:10px;align-items:center}
.lang-box{width:18px;height:12px;background:#c8d0e6}

/* hero */
.hero-title{left:0;width:1200px;top:250px;text-align:center;color:#fff;font-family:"Kaushan Script",cursive;font-size:88px;line-height:1}
.hero-sub{left:0;width:1200px;top:356px;text-align:center;color:#fff;font-family:"Poppins",sans-serif;font-weight:700;font-size:52px}
.arrow{width:36px;height:36px;border-radius:50%;background:#fff;display:flex;align-items:center;justify-content:center}

/* about */
.about-text{left:157px;top:800px;width:440px;font-size:19px;line-height:26.5px}
.frame-red{left:758px;top:686px;width:282px;height:369px;background:var(--red)}
.photo{background:linear-gradient(180deg,#d9d4cc 0%,#c9b08a 55%,#8a5a32 100%)}

/* products */
.card{width:209px;height:273px;background:var(--gold);padding:10px}
.card-inner{width:100%;height:100%;background:linear-gradient(160deg,#f6f6f6,#e6e2dc)}
.card-label{width:209px;text-align:center;font-size:19px;line-height:26px;color:#111}

/* work */
.work-box{left:157px;top:1849px;width:505px;height:369px;background:var(--panel)}
.field{position:absolute;background:#fff;border-radius:18px;font-family:"Kaushan Script",cursive;font-size:17px;color:#222;padding:6px 18px}
.frame-gold{left:758px;top:1849px;width:282px;height:369px;background:var(--gold)}

/* social programs */
.program{width:433px;height:279px}
.program-frame{position:absolute;left:30px;top:20px;right:30px;bottom:20px;border:2px solid rgba(255,255,255,.85);display:flex;align-items:center;justify-content:center;text-align:center;color:#fff;font-family:"Poppins",sans-serif;font-weight:700;font-size:31px;line-height:42px}

/* footer */
.footer-cols h4{font-family:"Poppins",sans-serif;font-weight:600;font-size:17px;color:#1a1a1a;position:absolute}
.flink{position:absolute;font-size:15px;color:#2a1a0a}
.thumb{position:absolute;width:52px;height:50px;background:linear-gradient(135deg,#6b3a34,#c43a36)}
</style>
</head>
<body>

<svg class="waves" viewBox="0 0 1200 3683" aria-hidden="true">
  <!-- hero photo area -->
  <defs>
    <linearGradient id="heroTone" x1="0" y1="0" x2="1" y2="1">
      <stop offset="0" stop-color="#e2a418"/>
      <stop offset=".5" stop-color="#d99a14"/>
      <stop offset="1" stop-color="#c68510"/>
    </linearGradient>
  </defs>
  <path d="M0,570 Q600,700 1200,575 L1200,595 Q600,660 0,585 Z" fill="var(--red)"/>
  <path d="M0,94 H1200 V555 Q600,700 0,550 Z" fill="url(#heroTone)"/>
  <!-- products white band -->
  <path d="M0,1185 Q600,1010 1200,1185 V1200 Q600,1030 0,1200 Z" fill="var(--red)"/>
  <path d="M0,1195 Q600,1030 1200,1195 V1690 H0 Z" fill="var(--white)"/>
  <!-- red work band -->
  <path d="M0,1680 Q600,1880 1200,1683 V2281 H0 Z" fill="var(--gold)"/>
  <path d="M0,1690 Q600,1870 1200,1693 V2281 H0 Z" fill="var(--red)"/>
  <!-- social programs white band -->
  <path d="M0,2281 H1200 V2724 Q600,2900 0,2724 Z" fill="var(--white)"/>
  <path d="M0,2724 Q600,2900 1200,2724 V2740 Q600,2885 0,2740 Z" fill="var(--red)"/>
  <!-- footer -->
  <path d="M0,3225 Q600,3130 1200,3225 V3250 Q600,3160 0,3250 Z" fill="var(--red)"/>
  <path d="M0,3245 Q600,3150 1200,3245 V3683 H0 Z" fill="var(--gold)"/>
  <line x1="157" y1="3346" x2="1043" y2="3346" stroke="#f7cf6a" stroke-width="1.5"/>
  <line x1="157" y1="3604" x2="1043" y2="3604" stroke="#f7cf6a" stroke-width="1.5"/>
</svg>

<!-- navigation -->
<header class="abs topbar"></header>
<div class="abs brand"><span class="brand-dot"></span>Tolvadera</div>
<nav class="abs menu">
  <span>The Company</span><span>Products</span><span>Job</span><span>Points of sale</span><span>Gallery</span><span>Contact</span>
</nav>
<div class="abs lang"><span class="lang-box"></span>
  <svg width="12" height="8" viewBox="0 0 12 8"><path d="M1 1l5 5 5-5" stroke="#fff" stroke-width="1.8" fill="none"/></svg>
</div>

<!-- hero -->
<div class="abs" role="img" aria-label="Farmer's hands holding a woven basket of corn cobs, warm golden tone" style="left:0;top:94px;width:1200px;height:10px"></div>
<div class="abs hero-title">Quality Low Prices</div>
<div class="abs hero-sub">Innovative Products</div>
<div class="btn" style="left:537px;top:442px;width:126px;height:37px">See Products</div>
<div class="abs arrow" style="left:158px;top:325px"><svg width="14" height="14" viewBox="0 0 14 14"><path d="M9 2L4 7l5 5" stroke="#222" stroke-width="2.4" fill="none"/></svg></div>
<div class="abs arrow" style="left:1006px;top:325px"><svg width="14" height="14" viewBox="0 0 14 14"><path d="M5 2l5 5-5 5" stroke="#222" stroke-width="2.4" fill="none"/></svg></div>

<!-- about -->
<h2 class="abs heading" style="left:156px;top:738px">ABOUT US</h2>
<p class="abs about-text">We are an industrial company belonging to the food sector that has the certifications that allow to prevent and control risk factors that guarantee the safety of the inputs used, thus guaranteeing the quality of our products.</p>
<div class="btn" style="left:157px;top:951px;width:125px;height:37px">Read More</div>
<div class="abs frame-red"></div>
<div class="abs photo" role="img" aria-label="Range of cereal and flour packages arranged on a wooden table" style="left:682px;top:697px;width:348px;height:347px"></div>

<!-- products -->
<h2 class="abs heading" style="left:0;width:1200px;text-align:center;top:1198px">OUR PRODUCTS</h2>
<div class="abs card" style="left:159px;top:1268px"><div class="card-inner" role="img" aria-label="Oatmeal with chocolate package"></div></div>
<div class="abs card" style="left:383px;top:1268px"><div class="card-inner" role="img" aria-label="Kiwicha and quinoa package"></div></div>
<div class="abs card" style="left:608px;top:1268px"><div class="card-inner" role="img" aria-label="Seven flours package"></div></div>
<div class="abs card" style="left:834px;top:1268px"><div class="card-inner" role="img" aria-label="Maca flour package"></div></div>
<div class="abs card-label" style="left:159px;top:1557px">OATMEAL</div>
<div class="abs card-label" style="left:383px;top:1557px">KIWICHA AND<br>QUINOA</div>
<div class="abs card-label" style="left:608px;top:1557px">OATMEAL</div>
<div class="abs card-label" style="left:834px;top:1557px">OATMEAL</div>
<div class="btn" style="left:537px;top:1637px;width:126px;height:37px">View All</div>

<!-- work with us -->
<section class="abs work-box">
  <h2 style="position:absolute;left:58px;top:30px;color:#fff;font-family:'Poppins',sans-serif;font-weight:700;font-size:34px">WORK WITH US</h2>
  <div class="field" style="left:60px;top:99px;width:191px;height:36px">Name</div>
  <div class="field" style="left:258px;top:99px;width:189px;height:36px">Age</div>
  <div class="field" style="left:60px;top:147px;width:191px;height:36px">Email</div>
  <div class="field" style="left:258px;top:147px;width:189px;height:36px">Profession</div>
  <div class="field" style="left:60px;top:195px;width:384px;height:88px;border-radius:4px;padding-top:10px">Message</div>
  <div class="btn" style="left:62px;top:293px;width:124px;height:36px">Subit Now</div>
</section>
<div class="abs frame-gold"></div>
<div class="abs" role="img" aria-label="Two colleagues sitting on grass reading a newspaper with a laptop" style="left:662px;top:1859px;width:368px;height:350px;background:linear-gradient(180deg,#c9cfc0 0%,#8d9a78 60%,#4e6a2e 100%)"></div>

<!-- social programs -->
<h2 class="abs heading" style="left:0;width:1200px;text-align:center;top:2376px">PRODUCTS FOR SOCIAL PROGRAMS</h2>
<div class="abs program" role="img" aria-label="Children in school, red tone" style="left:159px;top:2444px;background:linear-gradient(135deg,#d8302a,#b7231f)">
  <div class="program-frame">SUMAQ MIKUY<br>PROGRAM</div>
</div>
<div class="abs program" role="img" aria-label="Child drinking milk, gold tone" style="left:609px;top:2444px;background:linear-gradient(135deg,#eaaa10,#dea012)">
  <div class="program-frame">MORNING MILK<br>PROGRAM</div>
</div>

<!-- get in touch -->
<h2 class="abs heading" style="left:0;width:1200px;text-align:center;top:2910px">GET IN TOUCH</h2>
<div class="abs" style="left:360px;top:2979px;width:479px;height:51px;border:1.5px solid #555;background:#fff;display:flex;align-items:center;justify-content:center;gap:8px;font-size:16px;color:#333">
  <svg width="14" height="10" viewBox="0 0 14 10"><rect x=".5" y=".5" width="13" height="9" fill="#333"/><path d="M1 1l6 5 6-5" stroke="#fff" fill="none"/></svg>Enter Your mail ID
</div>
<div class="btn" style="left:538px;top:3045px;width:124px;height:37px">Submit Now</div>

<!-- footer -->
<div class="abs" style="left:0;width:1200px;top:3243px;text-align:center;font-family:'Poppins',sans-serif;font-size:28px;color:#1a1a1a;display:flex;justify-content:center;gap:34px;align-items:center">
  <span style="display:flex;align-items:center;gap:6px"><svg width="24" height="24" viewBox="0 0 24 24"><circle cx="12" cy="12" r="11" fill="#1a1a1a"/><path d="M8 6c1 0 2 3 1.5 3.5L8.6 10.4c.8 2 2.2 3.4 4 4.2l1-1c.5-.5 3.5.5 3.5 1.5 0 1.3-1.3 2.4-2.6 2.2C9.8 16.6 6.4 13.2 5.8 8.6 5.6 7.3 6.7 6 8 6z" fill="#fff"/></svg>CALL OR</span>
  <span style="display:flex;align-items:center;gap:6px"><svg width="26" height="26" viewBox="0 0 26 26"><circle cx="13" cy="13" r="12" fill="#1a1a1a"/></svg>CHATLINE NOW</span>
</div>
<div class="abs" style="left:0;width:1200px;top:3295px;text-align:center;font-family:'Poppins',sans-serif;font-weight:600;font-size:25px;color:var(--red);word-spacing:4px">(+51) 054-318220 &nbsp; / &nbsp; (+51) 054-627341 &nbsp; / &nbsp; (+51) 958413706</div>

<div class="footer-cols">
  <h4 style="left:157px;top:3392px">QUICK LINK</h4>
  <h4 style="left:360px;top:3392px">QUICK CONTACT</h4>
  <h4 style="left:704px;top:3392px">SOCIAL</h4>
  <h4 style="left:869px;top:3392px">GALLARY</h4>
</div>
<span class="flink" style="left:157px;top:3431px">The Company</span>
<span class="flink" style="left:157px;top:3462px">Products</span>
<span class="flink" style="left:157px;top:3494px">join up</span>
<span class="flink" style="left:157px;top:3525px">Contact</span>
<span class="flink" style="left:157px;top:3557px">Institutional Mail</span>

<svg class="abs" style="left:361px;top:3437px" width="12" height="16" viewBox="0 0 12 16"><path d="M6 0a6 6 0 0 1 6 6c0 4-6 10-6 10S0 10 0 6a6 6 0 0 1 6-6z" fill="#2a1a0a"/><circle cx="6" cy="6" r="2.2" fill="var(--gold)"/></svg>
<span class="flink" style="left:384px;top:3431px;line-height:22px">Calle Ribera Mz B2 Lot 7 PT<br>Los Alamos Cerro Verde - Arequipa</span>
<svg class="abs" style="left:361px;top:3503px" width="13" height="9" viewBox="0 0 13 9"><rect width="13" height="9" fill="#2a1a0a"/><path d="M.5 .5l6 4.5 6-4.5" stroke="var(--gold)" fill="none"/></svg>
<span class="flink" style="left:384px;top:3493px;line-height:22px">comercial@tolvadera.com /<br>administracion@tolvadera.com</span>

<span class="abs" style="left:705px;top:3436px;width:14px;height:14px;border-radius:50%;background:#2a1a0a"></span>
<span class="flink" style="left:727px;top:3432px">Fanpage</span>
<span class="abs" style="left:705px;top:3472px;width:14px;height:14px;border-radius:50%;background:#2a1a0a"></span>
<span class="flink" style="left:727px;top:3468px">Chirper</span>
<span class="abs" style="left:705px;top:3508px;width:14px;height:14px;border-radius:50%;background:#2a1a0a"></span>
<span class="flink" style="left:727px;top:3504px">ProNet</span>

<div class="thumb" role="img" aria-label="Event photo" style="left:872px;top:3438px"></div>
<div class="thumb" role="img" aria-label="Event photo" style="left:931px;top:3438px"></div>
<div class="thumb" role="img" aria-label="Event photo" style="left:990px;top:3438px"></div>
<div class="thumb" role="img" aria-label="Event photo" style="left:872px;top:3498px"></div>
<div class="thumb" role="img" aria-label="Event photo" style="left:931px;top:3498px"></div>
<div class="thumb" role="img" aria-label="Event photo" style="left:990px;top:3498px"></div>

<div class="abs" style="left:0;width:1200px;top:3630px;text-align:center;font-size:16px;color:#2a1a0a">Copyright©2021 tolvadera , All Rights Reserved.</div>

</body>
</html>
```